Flyer: helping to close the Global Digital Divide- V20 project.

We need a flyer designing for a nonprofit (www.brambleloop.org) based in Washington DC and London. We help to connect communities that have no internet so that they can get access to the health, educational, socio-economic benefits of internet connectivity. The project is ‘V20’ – internet for the Vital 20%.
The flyer will be sent to major corporations, governments, major universities, and the like.
The first half of the flyer will be design rich and incorporate the words (on the attached V20 document) in a creative and appealing way using design and color contrasts to highlight important points. The V20 Logo is attached also. I have also attached a similar but different PLRT document to give some ideas.
The second half of the flyer will be an MOU (Memorandum of Understanding) for the corporations to sign. This needs to be simple and look professional.
It is very important that we can change the words in the flyer once the design is complete without having to go back to the designer every time.

```html
<!DOCTYPE html>
<html lang="en">
<head>
<meta charset="utf-8">
<title>Memorandum of Understanding</title>
<link href="https://fonts.googleapis.com/css2?family=Montserrat:wght@400;600;700;800&display=swap" rel="stylesheet">
<style>
  :root {
    --ink: #1a1a1a;
    --paper: #ffffff;
    --band-start: #1c2d62;
    --band-end: #1a0d2a;
    --accent: #2ee6cf;
    --rule: #000000;
  }
  * { box-sizing: border-box; margin: 0; padding: 0; }
  html, body { width: 848px; height: 1200px; overflow: hidden; background: var(--paper); }
  .page {
    position: relative;
    width: 848px;
    height: 1200px;
    overflow: hidden;
    font-family: "Montserrat", sans-serif;
    color: var(--ink);
    background: var(--paper);
  }
  .network {
    position: absolute;
    pointer-events: none;
  }
  .network--top {
    top: 0; right: 0; width: 260px; height: 380px;
    background: radial-gradient(ellipse at 75% 30%, rgba(46,230,207,0.22), rgba(46,230,207,0) 70%);
  }
  .network--bottom {
    bottom: 0; right: 0; width: 640px; height: 580px;
    background: radial-gradient(ellipse at 70% 70%, rgba(46,230,207,0.20), rgba(46,230,207,0) 70%);
  }
  .title-band {
    position: absolute;
    left: 0; top: 73px;
    width: 627px; height: 136px;
    background: linear-gradient(90deg, var(--band-start), var(--band-end));
    padding: 24px 0 0 55px;
  }
  .title-band h1 {
    color: var(--paper);
    font-weight: 700;
    font-size: 41px;
    line-height: 52px;
    letter-spacing: 0.5px;
  }
  .intro {
    position: absolute;
    left: 55px; top: 232px;
    width: 760px;
    font-size: 14.6px;
    line-height: 18.8px;
  }
  .signatures {
    position: absolute;
    left: 53px; top: 501px;
    width: 740px;
    border-collapse: collapse;
    table-layout: fixed;
  }
  .signatures td {
    border: 3px solid var(--rule);
    font-weight: 700;
    font-size: 15px;
    padding: 0 0 0 16px;
    vertical-align: middle;
  }
  .signatures tr:nth-child(1) td { height: 44px; }
  .signatures tr:nth-child(2) td { height: 43px; }
  .signatures tr:nth-child(3) td { height: 43px; }
  .signatures tr:nth-child(4) td { height: 44px; }
  .signatures tr:nth-child(5) td { height: 43px; }
  .signatures tr:nth-child(6) td { height: 51px; }
  .terms {
    position: absolute;
    left: 55px; top: 804px;
    width: 740px;
  }
  .terms h2 {
    font-weight: 700;
    font-size: 20.5px;
    line-height: 28px;
    margin-bottom: 22px;
  }
  .clause {
    font-size: 14.6px;
    line-height: 18.8px;
    margin-bottom: 18px;
    padding-left: 2px;
  }
  .clause strong { font-weight: 600; }
</style>
</head>
<body>
<div class="page">
  <div class="network network--top" role="img" aria-label="Decorative teal network of connected points"></div>
  <div class="network network--bottom" role="img" aria-label="Decorative teal network of connected points"></div>

  <header class="title-band">
    <h1>MEMORANDUM<br>OF UNDERSTANDING</h1>
  </header>

  <section class="intro">
    <p>This Memorandum of Understanding (“MOU”) is entered into between:</p>
    <p>Brambleloop Foundation, a 501(c)(3) nonprofit corporation, with its principal place of business at 48 North Willow Lane, Fairmont VA, 22410 USA (“BLF”); and</p>
    <p>[Company], a [type of company] with it principle place business at [Address] (“Company”).</p>
    <p>The effective date of this MOU is [Date] (“Effective Date’) and the expiration date of this MOU is [Date] (“Expiration Date”).</p>
    <p>“CNDA” means the Corporate Non-Disclosure Agreement No. [CNDA reference number], dated [Date], entered into by the Parties.</p>
    <p>In this MOU, BLF and Company are sometimes referred to individually as a “Party” or collectively as “Parties.”</p>
    <p>BLF and Company wish to record in writing their non-binding proposals regarding potential engagement(s), as described in the attached Schedule (“Engagement”).</p>
  </section>

  <table class="signatures">
    <tr><td>FOR AND ON BEHALF OF BLF</td><td>FOR AND ON BEHALF OF COMPANY</td></tr>
    <tr><td>BY:</td><td>BY:</td></tr>
    <tr><td>PRINT NAME:</td><td>PRINT NAME:</td></tr>
    <tr><td>TITLE:</td><td>TITLE:</td></tr>
    <tr><td>SIGNED:</td><td>SIGNED:</td></tr>
    <tr><td>DATE:</td><td>DATE:</td></tr>
  </table>

  <section class="terms">
    <h2>THE PARTIES HEREBY AGREE AS FOLLOWS:</h2>
    <p class="clause"><strong>1. Non-Binding Nature:</strong> The Schedule to this MOU and its contents are not legally binding. Except for the obligations in Sections 1 to 10 and as specified in attached Exhibit A, which are all legally binding, no contract for the Engagement will exist unless and until the authorized representatives of each Party sign a separate legally binding written agreement.</p>
    <p class="clause"><strong>2. Term and Termination:</strong> This MOU will be effective on the Effective Date and will expire on the earlier of (a) the Expiration Date or (b) the date on which the Parties enter into a separate legally binding signed agreement relating to the Engagement. Either Party can, at any time for any reason and without any liability, end negotiations or terminate this MOU immediately upon giving written notice to the other Party. Sections 1, 2, 4, 8, and 9 of this MOU will survive termination of this MOU.]</p>
    <p class="clause"><strong>3. Expenses:</strong> Each Party is responsible for its own expenses in connection with all matters related to this MOU.</p>
  </section>
</div>
</body>
</html>
```